Website Development for vaultmeridian.com.au

Build a new Wordpress/Responsive website for vaultmeridian.com.au

Target Market(s)

Compliance Managers, Risk Managers, Information Security and Cyber Security Professionals, Chief Data/Digital Officers, Chief Operating/Financial Officers, Business Continuity Professionals, Disaster Recovery Planners, Small Business Owners, Local/Federal Government entities

Industry/Entity Type

Data Service

Coding

Coded - Design and coding required

Number of Pages Required

5+ page

Font styles to use
Sans Serif

Colors

Designer to choose colors to be used in the design.

Requirements
Must have
• 1. Site Structure: Home Page plus the following chapter-pages for a) Services b) About c) Resources d) Blog e) Contact Us
• 2. Prefer site to built on wordpress and we can purchase a theme if needed (we currently use Kivo for other sites)
• 3. Blog needs to be wordpress based
• 4. We will host the site ourselves on our own servers
• 5. Responsive Design
Nice to have
• 1. Livechat capability/interface
• 2. Capability for marketing automation integration (such as hubspot, marketo, infusionsoft etc)
• 3. Capability for CRM integration (Salesforce)

```html
<!DOCTYPE html>
<html lang="en">
<head>
<meta charset="utf-8">
<title>Vault Meridian – Cloud Solutions</title>
<link href="https://fonts.googleapis.com/css2?family=Lato:ital,wght@0,400;0,700;0,900;1,400&display=swap" rel="stylesheet">
<style>
:root{
  --red:#e31e24;
  --ink:#1b1d22;
  --text:#4a4d55;
  --muted:#8a8d94;
  --dark:#22262e;
  --dark-2:#2c313a;
  --footer:#1c1f25;
  --grey-bar:#7f8188;
  --white:#fff;
  --line:#e6e7ea;
}
*{box-sizing:border-box;margin:0;padding:0}
html,body{width:1200px;height:3163px;overflow:hidden}
body{font-family:'Lato',sans-serif;color:var(--text);background:var(--white);position:relative}
.wrap{position:absolute;left:250px;width:700px}
a{color:inherit;text-decoration:none}
.btn{display:inline-block;background:var(--red);color:var(--white);font-size:9px;font-weight:900;letter-spacing:.6px;text-transform:uppercase;text-align:center;line-height:32px;height:32px}

/* header */
.site-header{position:absolute;top:0;left:0;width:1200px;height:76px;background:var(--white)}
.brand{position:absolute;left:250px;top:20px;display:flex;align-items:center;gap:8px}
.brand-mark{width:22px;height:22px;background:var(--red)}
.brand-name{font-size:24px;font-weight:900;color:var(--ink);letter-spacing:-.3px}
.topbar{position:absolute;right:250px;top:10px;display:flex;align-items:center;gap:16px;font-size:9px;color:var(--muted)}
.topbar .item{display:flex;align-items:center;gap:5px}
.social{display:flex;gap:4px}
.social span{width:14px;height:14px;background:var(--red);display:block}
.main-nav{position:absolute;right:250px;top:52px;display:flex;gap:22px;font-size:8.5px;font-weight:700;color:var(--text)}
.main-nav a{position:relative}
.main-nav a.active{color:var(--red)}
.main-nav a.active:after{content:"";position:absolute;left:0;right:0;bottom:-10px;height:2px;background:var(--red)}
.divider{position:absolute;left:430px;top:36px;width:520px;height:1px;background:var(--line)}

/* hero */
.hero{position:absolute;top:76px;left:0;width:1200px;height:409px;background:linear-gradient(100deg,#0f1a33 0%,#1c2745 35%,#3a3d48 60%,#6b625a 100%)}
.hero-photo{position:absolute;inset:0}
.hero-shade{position:absolute;inset:0;background:linear-gradient(90deg,rgba(10,14,24,.55),rgba(10,14,24,.1) 70%)}
.hero h1{position:absolute;left:250px;top:112px;font-size:33px;font-weight:900;line-height:1.05;color:var(--white);letter-spacing:-.3px}
.hero p{position:absolute;left:250px;top:197px;width:460px;font-size:11px;line-height:1.5;color:#e4e6ec}
.hero .btn{position:absolute;left:250px;top:257px;width:101px}
.dots{position:absolute;left:570px;top:380px;display:flex;gap:6px}
.dots i{width:6px;height:6px;border-radius:50%;background:var(--red);opacity:.55;display:block}
.dots i:first-child{opacity:1}

/* section titles */
.sec-title{font-size:30px;font-weight:900;color:var(--ink);letter-spacing:-.3px}
.sec-title.center{text-align:center;color:var(--white)}
.rule{width:34px;height:3px;background:var(--red);margin-top:10px}
.center .rule,.rule.c{margin-left:auto;margin-right:auto}

/* about */
.about{top:540px}
.about .text{position:absolute;left:0;top:0;width:330px}
.about p{font-size:10.5px;line-height:1.55;margin-top:14px}
.about .btn{margin-top:24px;width:101px}
.video{position:absolute;left:360px;top:8px;width:340px;height:249px;background:radial-gradient(ellipse at 55% 70%,#4a4f5a 0%,#22252c 55%,#15171b 100%)}
.video .label{position:absolute;left:0;right:0;top:112px;text-align:center;font-size:26px;font-weight:900;color:var(--red)}
.play{position:absolute;left:146px;top:80px;width:48px;height:48px;border-radius:50%;border:3px solid var(--white)}
.play:after{content:"";position:absolute;left:17px;top:11px;border-left:16px solid var(--white);border-top:10px solid transparent;border-bottom:10px solid transparent}

/* services */
.services-band{position:absolute;top:861px;left:0;width:1200px;height:472px;background:linear-gradient(120deg,#1e222a,#2e343e 50%,#1f232a)}
.services{top:914px}
.cards{position:absolute;top:81px;left:0;width:700px;display:grid;grid-template-columns:repeat(3,228px);gap:19px 8px}
.card{background:var(--white);height:250px;position:relative;box-shadow:0 6px 16px rgba(0,0,0,.12);text-align:center}
.card svg{position:absolute;left:94px;top:38px;width:40px;height:40px}
.card h3{position:absolute;left:0;right:0;top:115px;font-size:13px;font-weight:700;color:var(--ink)}
.card p{position:absolute;left:30px;right:30px;top:140px;font-size:9px;line-height:1.45;color:var(--muted)}
.card .more{position:absolute;left:0;right:0;bottom:0;height:28px;line-height:28px;background:var(--grey-bar);color:var(--white);font-size:7.5px;font-weight:900;letter-spacing:.6px}
.services .all{position:absolute;left:290px;top:630px;width:121px}

/* stories */
.stories{top:1663px}
.quotes{position:absolute;top:80px;left:0;width:700px;display:grid;grid-template-columns:1fr 1fr;gap:34px}
.quote .mark{font-size:34px;font-weight:900;color:var(--red);line-height:.6;font-family:Georgia,serif}
.quote blockquote{font-size:13px;font-style:italic;line-height:1.45;color:var(--text);margin:10px 0 0 20px}
.person{display:flex;align-items:center;gap:8px;margin:16px 0 0 20px}
.avatar{width:30px;height:30px;border-radius:50%;background:#8c8f96}
.person b{display:block;font-size:10px;color:var(--ink)}
.person span{font-size:8.5px;color:var(--muted)}

/* blog */
.blog-band{position:absolute;top:1987px;left:0;width:1200px;height:396px;background:linear-gradient(120deg,#1e222a,#2c323b 55%,#1d2128)}
.blog{top:2040px}
.posts{position:absolute;top:73px;left:0;width:700px;display:grid;grid-template-columns:342px 339px;gap:19px}
.post{background:var(--white);height:369px;position:relative;box-shadow:0 6px 16px rgba(0,0,0,.12)}
.post .photo{height:190px}
.post .date{position:absolute;left:10px;top:10px;width:30px;height:32px;background:var(--red);color:var(--white);text-align:center;font-size:13px;font-weight:900;line-height:1.1;padding-top:4px}
.post .date small{display:block;font-size:6.5px;letter-spacing:.5px}
.post h3{margin:18px 18px 0;font-size:14.5px;font-weight:900;color:var(--ink);line-height:1.2}
.post p{margin:10px 18px 0;font-size:9px;line-height:1.5;color:var(--muted)}
.post .more{position:absolute;left:0;right:0;bottom:0;height:31px;line-height:31px;text-align:center;background:var(--grey-bar);color:var(--white);font-size:7.5px;font-weight:900;letter-spacing:.6px}
.blog .all{position:absolute;left:290px;top:474px;width:121px}

/* partners */
.partners{position:absolute;top:2664px;left:280px;width:640px;display:flex;justify-content:space-between;align-items:center}
.badge{height:32px;background:#d5d8dd;border-radius:4px}

/* footer */
.site-footer{position:absolute;top:2797px;left:0;width:1200px;height:366px;background:var(--footer);color:#c9ccd3}
.cols{position:absolute;left:242px;top:60px;width:740px;display:grid;grid-template-columns:184px 186px 184px 1fr}
.cols h4{font-size:10px;font-weight:900;color:var(--white);letter-spacing:.4px;margin-bottom:20px}
.cols li{list-style:none;font-size:9.5px;line-height:28px}
.foot-line{position:absolute;left:242px;right:250px;top:305px;height:1px;background:#2f333b}
.copy{position:absolute;left:242px;top:335px;font-size:9px;color:#7e828a}
.copy b{color:#c9ccd3;font-weight:400}
.foot-social{position:absolute;left:800px;top:336px;display:flex;gap:16px}
.foot-social span{width:7px;height:7px;background:#c9ccd3;display:block}
.to-top{position:absolute;left:893px;top:322px;width:28px;height:28px;background:var(--red)}
.to-top svg{position:absolute;left:8px;top:8px}
</style>
</head>
<body>

<header class="site-header">
  <a class="brand" href="#"><span class="brand-mark"></span><span class="brand-name">Vault Meridian</span></a>
  <div class="topbar">
    <span class="item"><svg width="10" height="8" viewBox="0 0 10 8"><rect x=".5" y=".5" width="9" height="7" fill="none" stroke="#e31e24"/><path d="M.5 .5 5 4.5 9.5 .5" fill="none" stroke="#e31e24"/></svg>info@vaultmeridian.com.au</span>
    <span class="item"><svg width="9" height="9" viewBox="0 0 10 10"><path d="M2 0h2l1 3-1.5 1a6 6 0 0 0 2.5 2.5L7 5l3 1v2a2 2 0 0 1-2 2A8 8 0 0 1 0 2a2 2 0 0 1 2-2z" fill="#e31e24"/></svg>(123) 456 7890</span>
    <span class="social"><span></span><span></span><span></span></span>
  </div>
  <div class="divider"></div>
  <nav class="main-nav">
    <a class="active" href="#">HOME</a><a href="#">SERVICES ▾</a><a href="#">ABOUT</a><a href="#">RESOURCES</a><a href="#">BLOG</a><a href="#">CONTACT</a>
  </nav>
</header>

<section class="hero">
  <div class="hero-photo" role="img" aria-label="Woman with a laptop standing in a server room corridor"></div>
  <div class="hero-shade"></div>
  <h1>VAULT MERIDIAN<br>CLOUD SOLUTIONS</h1>
  <p>Nullam adversarium cu mea, id ridens percipitur mei, nec tale voluptua comprehensam ei vix numquam persequeris interesset, mei partem gubergren eu, tota harum te mei.</p>
  <a class="btn" href="#">Learn more</a>
  <div class="dots"><i></i><i></i><i></i><i></i><i></i></div>
</section>

<section class="wrap about">
  <div class="text">
    <h2 class="sec-title">ABOUT US</h2>
    <div class="rule"></div>
    <p>Lorem ipsum dolor sit amet, eu stet paulo docendi est. Probo apparent scriptorem his ut, mel cu alii causae. In medius aliquam expetendis vix. Id paulo dissentiunt pri. Prima liber ei vis, sea eu denique recteque molestiae. Id has eloquentiam definitiones, lorem dicta in has, ei delenit gubergren sed.</p>
    <p>Te dicta dissentias ius, eu pri facete impedit pertinax. Dolores definiebas ius ne. Eius homero meliore eos te. Usu ficer ceteros eum cu legimus eligendi appareat, dicunt salutandi consectetuer eorum.</p>
    <a class="btn" href="#">Learn more</a>
  </div>
  <div class="video" role="img" aria-label="Company video still over a dark dotted digital landscape">
    <div class="label">Vault Meridian</div>
    <div class="play"></div>
  </div>
</section>

<div class="services-band"></div>
<section class="wrap services">
  <h2 class="sec-title center">SERVICES<div class="rule"></div></h2>
  <div class="cards">
    <article class="card">
      <svg viewBox="0 0 40 40" fill="none" stroke="#e31e24" stroke-width="2"><circle cx="11" cy="10" r="4"/><circle cx="20" cy="8" r="4"/><circle cx="29" cy="10" r="4"/><path d="M6 32V20a5 5 0 0 1 10 0v12M15 30V18a5 5 0 0 1 10 0v12M24 32V20a5 5 0 0 1 10 0v12"/></svg>
      <h3>Security Intelligence</h3><p>Causae audiam facilis id sit. Mea ne laoreet torquatos scriptorem, eum eu augue prompta ornatus.</p><div class="more">LEARN MORE</div>
    </article>
    <article class="card">
      <svg viewBox="0 0 40 40" fill="none" stroke="#e31e24" stroke-width="2"><path d="M4 10h12l3 4h17v20H4z"/><path d="M20 18l6 2v5c0 4-3 6-6 7-3-1-6-3-6-7v-5z"/><path d="M17 25l2 2 4-4"/></svg>
      <h3>Data Security</h3><p>Causae audiam facilis id sit. Mea ne laoreet torquatos scriptorem, eum eu augue prompta ornatus.</p><div class="more">LEARN MORE</div>
    </article>
    <article class="card">
      <svg viewBox="0 0 40 40" fill="none" stroke="#e31e24" stroke-width="2"><circle cx="16" cy="12" r="7"/><path d="M4 34c0-8 5-12 12-12 3 0 5 .5 7 2"/><path d="M29 22l6 2v5c0 3-3 5-6 6-3-1-6-3-6-6v-5z"/></svg>
      <h3>Identity Security</h3><p>Causae audiam facilis id sit. Mea ne laoreet torquatos scriptorem, eum eu augue prompta ornatus.</p><div class="more">LEARN MORE</div>
    </article>
    <article class="card">
      <svg viewBox="0 0 40 40" fill="none" stroke="#e31e24" stroke-width="2"><rect x="8" y="4" width="24" height="8"/><rect x="8" y="14" width="24" height="8"/><rect x="8" y="24" width="24" height="8"/><path d="M20 32v4M10 36h20M12 8h2M12 18h2M12 28h2"/></svg>
      <h3>Network Security</h3><p>Causae audiam facilis id sit. Mea ne laoreet torquatos scriptorem, eum eu augue prompta ornatus.</p><div class="more">LEARN MORE</div>
    </article>
    <article class="card">
      <svg viewBox="0 0 40 40" fill="none" stroke="#e31e24" stroke-width="2"><rect x="11" y="3" width="18" height="34" rx="2"/><path d="M18 33h4"/><path d="M20 12l6 2v5c0 3-3 5-6 6-3-1-6-3-6-6v-5z"/></svg>
      <h3>Mobile Security</h3><p>Causae audiam facilis id sit. Mea ne laoreet torquatos scriptorem, eum eu augue prompta ornatus.</p><div class="more">LEARN MORE</div>
    </article>
    <article class="card">
      <svg viewBox="0 0 40 40" fill="none" stroke="#e31e24" stroke-width="2"><rect x="4" y="6" width="32" height="28" rx="2"/><path d="M4 13h32M8 9.5h2M12 9.5h2"/><path d="M20 17l6 2v4c0 3-3 5-6 6-3-1-6-3-6-6v-4z"/></svg>
      <h3>Application Security</h3><p>Causae audiam facilis id sit. Mea ne laoreet torquatos scriptorem, eum eu augue prompta ornatus.</p><div class="more">LEARN MORE</div>
    </article>
  </div>
  <a class="btn all" href="#">View all services</a>
</section>

<section class="wrap stories">
  <h2 class="sec-title">SUCCESS STORIES</h2>
  <div class="rule"></div>
  <div class="quotes">
    <div class="quote">
      <div class="mark">“</div>
      <blockquote>Munere detracto repudiandae vis no, mollis alienum in qui sed id quaestio laboramus, ei mei altera postulant rationibus usu ferri ullum ex.</blockquote>
      <div class="person"><div class="avatar" role="img" aria-label="Client portrait"></div><div><b>Maren Holt</b><span>XYZ LLC</span></div></div>
    </div>
    <div class="quote">
      <div class="mark">“</div>
      <blockquote>Ei quando feugait maluisset sit ceteros inter pretoris quo ex, qui eu mutat vitae vidisse nostro appetere erroribus qui, dicant placerat mnesarchum ex mea.</blockquote>
      <div class="person"><div class="avatar" role="img" aria-label="Client portrait"></div><div><b>Theo Lindqvist</b><span>ABC LLC</span></div></div>
    </div>
  </div>
</section>

<div class="blog-band"></div>
<section class="wrap blog">
  <h2 class="sec-title center">FROM THE BLOG<div class="rule"></div></h2>
  <div class="posts">
    <article class="post">
      <div class="photo" role="img" aria-label="Team gathered around a laptop in a bright office" style="background:linear-gradient(135deg,#c9c6c0,#7d7a78 60%,#5b5a5e)"></div>
      <div class="date">19<small>FEB</small></div>
      <h3>Nullam adversarium cu mea id ridens percipitur mei, nec tale voluptua compru hensam ei</h3>
      <p>Ancillae corrumpit ut mea. Id vis numquam persecuti interesset, mel partem gubergren eu, tota harum te mel. Pri ne mentitum antiopam voluptatibus, in omnis patent lucilius sed...</p>
      <div class="more">READ MORE</div>
    </article>
    <article class="post">
      <div class="photo" role="img" aria-label="Speaker presenting to an audience in a conference room" style="background:linear-gradient(180deg,#b8b5b0,#8a8680 55%,#4d4a48)"></div>
      <div class="date">11<small>FEB</small></div>
      <h3>Ad has integre deleniti, graeco apeirian tractatos no quo, mea debet simul expetendis ne</h3>
      <p>Ancillae corrumpit ut mea. Id vis numquam persecuti interesset, mel partem gubergren eu, tota harum te mel. Pri ne mentitum antiopam voluptatibus, in omnis patent lucilius sed...</p>
      <div class="more">READ MORE</div>
    </article>
  </div>
  <a class="btn all" href="#">View all posts</a>
</section>

<div class="partners" aria-label="Technology partners">
  <div class="badge" style="width:80px"></div>
  <div class="badge" style="width:96px"></div>
  <div class="badge" style="width:98px"></div>
  <div class="badge" style="width:106px"></div>
  <div class="badge" style="width:76px"></div>
</div>

<footer class="site-footer">
  <div class="cols">
    <div><h4>COMPANY</h4><ul><li>Company</li><li>Patents</li><li>People</li><li>Locations</li><li>Careers</li></ul></div>
    <div><h4>SERVICES</h4><ul><li>Security Intelligence</li><li>Data Security</li><li>Identity Security</li><li>Network Security</li><li>Mobile Security</li><li>View All Services</li></ul></div>
    <div><h4>PARTNERS</h4><ul><li>Partner Program</li><li>Partner Network</li><li>Become a Partner</li></ul></div>
    <div><h4>CUSTOMERS</h4><ul><li>Use Cases</li><li>Success Stories</li><li>Support</li></ul></div>
  </div>
  <div class="foot-line"></div>
  <div class="copy">Copyright © 2019 <b>Vault Meridian</b></div>
  <div class="foot-social"><span></span><span></span><span></span></div>
  <a class="to-top" href="#" aria-label="Back to top"><svg width="12" height="12" viewBox="0 0 12 12"><path d="M2 8l4-4 4 4" fill="none" stroke="#fff" stroke-width="2"/></svg></a>
</footer>

</body>
</html>
```